Eastfield Commercial Card

I would like a modern, eye catching card based off my logo design.
Info to include:
Anders Voll (Card Name)
eastfieldcommercial.example (Website)
555 203 8841 (Office/fax)
555 287 3096 (Business Cell)
anders@eastfieldcommercial.example (Work email)

Target Market(s)

Commercial real estate brokers, property owners.

Colors
ec1f27
757575

Requirements
Must have
• Name and info above. Not be lame!:)

```html
<!DOCTYPE html>
<html lang="en">
<head>
<meta charset="utf-8">
<title>Eastfield Commercial Business Card</title>
<link href="https://fonts.googleapis.com/css2?family=Arimo:wght@400;700&display=swap" rel="stylesheet">
<style>
  :root {
    --brand-red: #b01e26;
    --brand-grey: #757575;
    --charcoal: #3b3b3b;
    --ink: #1c1c1c;
    --paper: #ffffff;
    --backdrop: #e9e9e9;
  }
  * { box-sizing: border-box; margin: 0; padding: 0; }
  html, body { width: 1200px; height: 997px; overflow: hidden; }
  body {
    background: var(--backdrop);
    font-family: "Arimo", Arial, sans-serif;
    position: relative;
  }
  .card {
    position: absolute;
    left: 300px;
    width: 600px;
    height: 343px;
    background: var(--paper);
    border-radius: 16px;
    overflow: hidden;
    box-shadow: 0 6px 18px rgba(0,0,0,0.18);
  }
  .card--front { top: 110px; }
  .card--back { top: 520px; }
  .card__band { position: absolute; left: 0; bottom: 0; width: 600px; height: 90px; }

  .brand-name {
    display: flex;
    align-items: center;
    gap: 12px;
    font-family: "Arimo", sans-serif;
    font-weight: 700;
    color: var(--charcoal);
    white-space: nowrap;
  }
  .brand-name__mark { flex: none; background: var(--brand-red); }
  .tagline {
    font-family: "Arimo", sans-serif;
    font-weight: 400;
    color: var(--brand-grey);
    letter-spacing: 2px;
    text-transform: uppercase;
    white-space: nowrap;
  }

  /* Front */
  .front__brand {
    position: absolute; left: 0; right: 0; top: 112px;
    display: flex; flex-direction: column; align-items: center;
  }
  .front__brand .brand-name { font-size: 34px; }
  .front__brand .brand-name__mark { width: 26px; height: 26px; }
  .front__brand .tagline { font-size: 14px; margin-top: 10px; }
  .front__address {
    position: absolute;
    right: 26px;
    bottom: 14px;
    color: var(--paper);
    font-weight: 700;
    font-size: 15px;
  }

  /* Back */
  .back__brand { position: absolute; left: 34px; top: 36px; }
  .back__brand .brand-name { font-size: 24px; gap: 10px; }
  .back__brand .brand-name__mark { width: 18px; height: 18px; }
  .back__brand .tagline { font-size: 11px; margin-top: 6px; }
  .back__person { position: absolute; right: 34px; top: 98px; text-align: right; }
  .back__name {
    font-weight: 700;
    color: var(--brand-red);
    font-size: 18px;
    letter-spacing: 0.5px;
  }
  .back__title { color: var(--ink); font-size: 13px; margin-top: 2px; }
  .back__rule {
    position: absolute;
    left: 34px;
    right: 34px;
    top: 158px;
    height: 1px;
    background: var(--ink);
  }
  .contact-list {
    position: absolute;
    left: 34px;
    top: 182px;
    list-style: none;
  }
  .contact-list li {
    display: flex;
    align-items: center;
    gap: 10px;
    font-size: 15px;
    color: var(--ink);
    height: 24px;
  }
  .contact-icon { width: 16px; height: 16px; flex: none; }
  .back__web {
    position: absolute;
    right: 24px;
    bottom: 14px;
    color: var(--paper);
    font-weight: 700;
    font-size: 14px;
    letter-spacing: 0.5px;
  }
</style>
</head>
<body>

<section class="card card--front" aria-label="Card front">
  <div class="front__brand">
    <div class="brand-name"><span class="brand-name__mark"></span>Eastfield Commercial</div>
    <div class="tagline">Construction &amp; Roofing</div>
  </div>
  <svg class="card__band" viewBox="0 0 600 90" aria-hidden="true">
    <path d="M0 58 L240 58 Q260 58 272 48 L286 36 Q296 30 312 30 L600 30 L600 34 L316 34 Q300 34 292 40 L278 52 Q264 64 244 64 L0 64 Z" fill="var(--charcoal)"/>
    <path d="M0 74 L250 74 Q270 74 284 60 L296 50 Q306 44 322 44 L600 44 L600 90 L0 90 Z" fill="var(--brand-red)"/>
  </svg>
  <div class="front__address">482 Birchwood Lane Ashford MN 55000</div>
</section>

<section class="card card--back" aria-label="Card back">
  <div class="back__brand">
    <div class="brand-name"><span class="brand-name__mark"></span>Eastfield Commercial</div>
    <div class="tagline">Construction &amp; Roofing</div>
  </div>
  <div class="back__person">
    <div class="back__name">ANDERS VOLL</div>
    <div class="back__title">Director of Sales &amp; Marketing</div>
  </div>
  <div class="back__rule"></div>
  <ul class="contact-list">
    <li>
      <svg class="contact-icon" viewBox="0 0 16 16" aria-hidden="true"><circle cx="8" cy="8" r="8" fill="var(--brand-red)"/><path d="M4 6.5 Q8 3.5 12 6.5 L11 8 L9.5 7.2 L9.5 6.4 Q8 6 6.5 6.4 L6.5 7.2 L5 8 Z M5.5 9 H10.5 V11.5 H5.5 Z" fill="#fff"/></svg>
      555 203 8841
    </li>
    <li>
      <svg class="contact-icon" viewBox="0 0 16 16" aria-hidden="true"><circle cx="8" cy="8" r="8" fill="var(--brand-red)"/><rect x="5.5" y="3.5" width="5" height="9" rx="1" fill="#fff"/><rect x="6.3" y="4.5" width="3.4" height="6" fill="var(--brand-red)"/></svg>
      555 287 3096
    </li>
    <li>
      <svg class="contact-icon" viewBox="0 0 16 16" aria-hidden="true"><circle cx="8" cy="8" r="8" fill="var(--brand-red)"/><rect x="4" y="5" width="8" height="6" fill="#fff"/><path d="M4 5 L8 8.5 L12 5" stroke="var(--brand-red)" stroke-width="1" fill="none"/></svg>
      anders@eastfieldcommercial.example
    </li>
  </ul>
  <svg class="card__band" viewBox="0 0 600 90" aria-hidden="true">
    <path d="M0 58 L226 58 Q244 58 254 48 L264 38 Q272 32 286 32 L600 32 L600 36 L288 36 Q276 36 270 42 L260 52 Q248 64 230 64 L0 64 Z" fill="var(--charcoal)"/>
    <path d="M0 76 L236 76 Q254 76 266 64 L276 54 Q284 46 298 46 L600 46 L600 90 L0 90 Z" fill="var(--brand-red)"/>
  </svg>
  <div class="back__web">www.eastfieldcommercial.example</div>
</section>

</body>
</html>
```